Varden Institute for Restorative Care

I need a full informational website for my medical practice. I would like to use my logo and also include a lot of emblems/pictures (also a picture of me in a white coat). The website should have a function for people to inquire and send me messages. I will be offering needle-less regenerative injection therapy, stem cell treatments, bioidentical hormone therapy, treatment for chronic illness, neurodegenerative diseases, skin rejuvenation, hair restoration, male enhancement, female enhancement, and anti-aging. The practice will not be accepting insurance and will be cash/credit card only.
A good example of written content and functionality is this website:
http://thebrvx.example/. However, I want different theme and tones.
Target Market(s)
High end clientele in Los Angeles, Southern California. Health minded people who are interested in living better and longer and can afford anti-aging treatments. Men and women who want to improve sexual health and wellbeing.
Requirements
Must have
- 1. I will need to be able to move the site to other servers (needed for site speed)
- 2. Site must be build on WordPress
- 3. Full admin credentials for domain, cpanel, wordpress, ftp.
- 4. No third party interaction on development and content deployment once the site is on different servers
- 5. I will need the ability to add content and links to the site
- 6. I will need the ability to optimize the site for speed
- 7. I will need to ability to modify URLs so they are more SEO friendly
Nice to have
- pictures of stem cells, health improvement and regeneration, beauty, youthful individuals, older healthy and happy individuals. Medical designs.
Should not have
- flowers, dna

```html
<!DOCTYPE html>
<html lang="en">
<head>
<meta charset="utf-8">
<title>Varden Institute for Restorative Care</title>
<link rel="stylesheet" href="https://fonts.googleapis.com/css2?family=Lora:wght@400;600;700&display=swap">
<style>
:root{
  --green:#1aa98a;
  --green-dark:#12916f;
  --navy:#0e2a7c;
  --ink:#1e1e1e;
  --muted:#5a5a5a;
  --light:#f2f2f2;
  --hero-bg:#ececec;
  --footer:#1d1d1d;
  --white:#ffffff;
}
*{box-sizing:border-box;margin:0;padding:0}
html,body{width:1200px;height:4423px;overflow:hidden;background:var(--white)}
body{font-family:'Lora',serif;color:var(--ink)}
.canvas{position:relative;width:1200px;height:4423px;overflow:hidden}
.abs{position:absolute}
.btn{position:absolute;display:flex;align-items:center;justify-content:center;border-radius:16px;color:var(--white);font-size:13px;height:30px}
.btn-navy{background:var(--navy)}
.btn-green{background:var(--green)}
.photo{position:absolute}
.section-title{position:absolute;left:0;width:1200px;text-align:center;font-size:32px;font-weight:400}

/* header */
.brand{left:162px;top:22px;display:flex;align-items:center;gap:12px}
.brand-dot{width:46px;height:46px;border-radius:50%;background:var(--green)}
.brand-name{font-size:40px;font-weight:600;color:var(--navy);letter-spacing:2px}
.top-links{right:330px;top:50px;font-size:13px;color:var(--ink)}
.top-links span{margin:0 6px}
.cart{left:988px;top:42px;font-size:12px;line-height:16px;border-left:1px solid #ccc;padding-left:8px}
.cart-icon{left:1050px;top:42px;width:34px;height:34px;border-radius:50%;background:var(--navy)}
.nav{left:0;top:133px;width:1200px;height:50px;background:var(--green)}
.nav a{position:absolute;top:0;height:50px;line-height:50px;color:var(--white);font-size:14px;text-decoration:none;font-weight:600}
.nav .active{background:var(--green-dark);padding:0 30px}
.nav .send{background:var(--navy);top:9px;height:32px;line-height:32px;border-radius:16px;width:183px;text-align:center}

/* hero */
.hero{left:0;top:183px;width:1200px;height:540px;background:var(--hero-bg)}
.hero-title{left:118px;top:355px;font-size:36px;color:var(--ink)}
.hero-sub{left:118px;top:418px;font-size:15px}
.hero-text{left:118px;top:442px;width:380px;font-size:13px;line-height:18px;color:var(--muted)}
.arrow{width:32px;height:32px;border-radius:50%;background:#222;display:flex;align-items:center;justify-content:center}
.dots{display:flex;gap:7px}
.dots i{width:9px;height:9px;border-radius:50%;background:#444;display:block}
.dots i.on{background:#aaa}

/* about */
.about-kicker{left:628px;top:870px;font-size:14px}
.about-title{left:628px;top:895px;font-size:34px}
.about-text{left:628px;top:938px;width:460px;font-size:14px;line-height:21px;color:var(--muted)}

/* services */
.service{position:absolute;width:193px;text-align:center;color:var(--white);font-size:14px;line-height:18px}
.service .circ{width:177px;height:177px;border-radius:50%;margin:0 auto 10px;border:4px solid var(--white)}

/* products */
.product{position:absolute;width:241px;text-align:center;font-size:13px}
.product .pimg{height:221px;margin:0 auto 36px;width:200px}
.product .btn{position:relative;margin:8px auto 0;width:140px}

/* blog */
.card{position:absolute;top:2706px;width:308px;height:360px;background:var(--white);box-shadow:0 2px 6px rgba(0,0,0,.15)}
.card .cimg{height:192px;position:relative}
.card .badge{position:absolute;left:12px;top:0;width:32px;height:42px;background:var(--navy);color:var(--white);font-size:11px;text-align:center;line-height:14px;padding-top:6px}
.card h3{font-size:14px;font-weight:600;margin:16px 12px 4px;text-decoration:underline}
.card .meta{display:flex;justify-content:space-between;margin:0 12px;font-size:12px}
.card p{margin:8px 12px 0;font-size:12.5px;line-height:18px;color:var(--muted)}
.card .more{margin:10px 12px 0;font-size:12.5px}

/* testimonials */
.tcard{position:absolute;top:3375px;width:457px;height:162px;background:var(--light)}
.tcard .avatar{position:absolute;left:-4px;top:0;width:162px;height:162px;border-radius:50%;border:5px solid var(--white)}
.tcard .who{position:absolute;left:200px;top:22px;width:180px;text-align:center;font-size:14px;font-weight:600}
.tcard .role{position:absolute;left:200px;top:40px;width:180px;text-align:center;font-size:11px;color:var(--green)}
.tcard .quote{position:absolute;left:200px;top:58px;width:220px;font-size:12.5px;line-height:17px;color:var(--muted)}
.tcard .read{position:absolute;left:260px;top:124px;font-size:12px}
.qmark{position:absolute;font-size:40px;color:#999;line-height:40px}

/* features */
.feature{position:absolute;top:3758px;width:308px;height:177px;background:var(--light);text-align:center;font-size:14px}
.feature .ft{position:absolute;left:0;width:100%;top:100px;font-weight:600}
.feature .fs{position:absolute;left:0;width:100%;top:122px;font-size:12px}

/* footer */
.footer{left:0;top:4024px;width:1200px;height:339px;background:var(--footer);color:#ddd}
.fhead{font-size:15px;color:var(--white);font-weight:600}
.flist{font-size:12.5px;line-height:19.5px;list-style:none}
.flist li::before{content:"\203A";margin-right:10px}
.finfo{font-size:12.5px;line-height:26px}
.field{position:absolute;height:26px;background:#2e2e2e;font-size:11px;color:#999;padding:6px 8px}
.bottom{left:0;top:4363px;width:1200px;height:60px;background:var(--navy);color:var(--white);font-size:13px}
.social{position:absolute;top:15px;width:30px;height:30px;border-radius:50%;background:var(--white)}
</style>
</head>
<body>
<div class="canvas">

<!-- header -->
<div class="abs brand"><span class="brand-dot"></span><span class="brand-name">Varden</span></div>
<div class="abs top-links"><span>My Account</span>|<span>My Wishlist</span>|<span>Checkout</span></div>
<div class="abs cart">My Cart<br>$00.00</div>
<div class="abs cart-icon"></div>

<nav class="abs nav">
  <a class="active" style="left:124px">Home</a>
  <a style="left:265px">About us</a>
  <a style="left:392px">Services ▾</a>
  <a style="left:551px">Products</a>
  <a style="left:693px">Blogs</a>
  <a style="left:772px">Contact us</a>
  <svg class="abs" style="left:858px;top:17px" width="16" height="16" viewBox="0 0 16 16"><circle cx="6.5" cy="6.5" r="5" fill="none" stroke="#fff" stroke-width="2"/><path d="M10 10l5 5" stroke="#fff" stroke-width="2"/></svg>
  <a class="send" style="left:899px">Send A Message</a>
</nav>

<!-- hero -->
<section class="abs hero"></section>
<div class="photo" role="img" aria-label="Close-up portrait showing skin before and after anti-aging treatment" style="left:560px;top:183px;width:520px;height:530px;background:linear-gradient(90deg,#e8c9b3 0%,#d8ad92 50%,#c99b82 51%,#e2bfa8 100%)"></div>
<div class="abs hero-title">Anti-Aging</div>
<div class="abs hero-sub">Center For Regenerative Medicine</div>
<div class="abs hero-text">Lorem Ipsum is simply dummy text of the printing and typesetting industry.</div>
<div class="btn btn-navy" style="left:118px;top:498px;width:160px">Read More</div>
<div class="btn btn-green" style="left:324px;top:498px;width:126px">Shop Now</div>
<div class="abs arrow" style="left:44px;top:436px"><svg width="12" height="12" viewBox="0 0 12 12"><path d="M8 1L3 6l5 5" fill="none" stroke="#fff" stroke-width="2"/></svg></div>
<div class="abs arrow" style="left:1124px;top:436px;background:var(--navy)"><svg width="12" height="12" viewBox="0 0 12 12"><path d="M4 1l5 5-5 5" fill="none" stroke="#fff" stroke-width="2"/></svg></div>
<div class="abs dots" style="left:575px;top:660px"><i class="on"></i><i></i><i></i><i></i></div>
<svg class="abs" style="left:0;top:660px" width="1200" height="90" viewBox="0 0 1200 90"><path d="M0,30 C300,62 700,80 1200,20 L1200,90 L0,90 Z" fill="#fff"/><path d="M0,30 C300,62 700,80 1200,20" fill="none" stroke="#1aa98a" stroke-width="8"/></svg>

<!-- about -->
<div class="photo" role="img" aria-label="Video of a doctor with digital medical interface" style="left:118px;top:840px;width:462px;height:320px;background:linear-gradient(135deg,#1d3550,#5f7f9a 60%,#b9c7d2)"></div>
<svg class="abs" style="left:314px;top:965px" width="70" height="70" viewBox="0 0 70 70"><circle cx="35" cy="35" r="32" fill="rgba(255,255,255,.25)" stroke="#fff" stroke-width="3"/><path d="M28 22l20 13-20 13z" fill="#fff"/></svg>
<div class="abs about-kicker">How We Are</div>
<h2 class="abs about-title" style="font-weight:400">About us</h2>
<p class="abs about-text">Lorem Ipsum is simply dummy text of the printing and types industry. Lorem Ipsum has been the industry's standard dummy text ever since the 1500s,<br><br>when an unknown printer took a gallery of type and scrambled it to make a type specimen book.</p>
<div class="btn btn-navy" style="left:628px;top:1078px;width:162px">Read More</div>

<!-- services -->
<svg class="abs" style="left:0;top:1160px" width="1200" height="800" viewBox="0 0 1200 800"><path d="M0,25 C350,-15 800,110 1200,95 L1200,750 C800,735 380,800 0,775 Z" fill="#1aa98a"/></svg>
<div class="abs" style="left:0;top:1296px;width:1200px;text-align:center;color:#fff;font-size:13px;font-weight:600">We offer</div>
<h2 class="section-title" style="top:1313px;color:#fff">Our Services</h2>
<div class="service" style="left:118px;top:1385px"><div class="circ" style="background:linear-gradient(135deg,#e9c4a6,#c28d6c)" role="img" aria-label="Patient receiving needle-less injection therapy"></div>Needle-Less Regenerative Injection Therapy</div>
<div class="service" style="left:311px;top:1385px"><div class="circ" style="background:linear-gradient(135deg,#f2dcd0,#d6a993)" role="img" aria-label="Stem cell treatment skin care"></div>Stem Cell Treatments</div>
<div class="service" style="left:504px;top:1385px"><div class="circ" style="background:linear-gradient(135deg,#f4f4f6,#d0473d 70%,#3c6fb5)" role="img" aria-label="Hormone test sample tubes"></div>Bioidentical Hormone Therapy</div>
<div class="service" style="left:697px;top:1385px"><div class="circ" style="background:linear-gradient(135deg,#d9c7bb,#9a6e58)" role="img" aria-label="Man with chronic neck pain"></div>Treatment For Chronic Illness</div>
<div class="service" style="left:890px;top:1385px"><div class="circ" style="background:linear-gradient(135deg,#cfcfcf,#6a6a6a)" role="img" aria-label="Neuron cells microscope view"></div>Neurodegenerative Diseases</div>
<div class="service" style="left:118px;top:1663px"><div class="circ" style="background:linear-gradient(135deg,#cfd6da,#e9c9b5)" role="img" aria-label="Skin rejuvenation treatment"></div>Skin Rejuvenation</div>
<div class="service" style="left:311px;top:1663px"><div class="circ" style="background:linear-gradient(135deg,#c89c7e,#6b4a37)" role="img" aria-label="Man checking hair loss"></div>Hair Restoration</div>
<div class="service" style="left:504px;top:1663px"><div class="circ" style="background:linear-gradient(135deg,#efe2d6,#b98466)" role="img" aria-label="Confident healthy man"></div>Male Enhancement</div>
<div class="service" style="left:697px;top:1663px"><div class="circ" style="background:linear-gradient(135deg,#e3d4cf,#6f86a8)" role="img" aria-label="Woman consulting on wellbeing"></div>Female Enhancement</div>
<div class="service" style="left:890px;top:1663px"><div class="circ" style="background:linear-gradient(135deg,#efd7c6,#b68a70)" role="img" aria-label="Woman examining her skin"></div>Anti-Aging.</div>

<!-- products -->
<h2 class="section-title" style="top:2014px">Feature Product</h2>
<div class="abs arrow" style="left:1024px;top:2022px;width:24px;height:24px"><svg width="10" height="10" viewBox="0 0 12 12"><path d="M8 1L3 6l5 5" fill="none" stroke="#fff" stroke-width="2"/></svg></div>
<div class="abs arrow" style="left:1054px;top:2022px;width:24px;height:24px;background:#fff;border:2px solid #222"><svg width="10" height="10" viewBox="0 0 12 12"><path d="M4 1l5 5-5 5" fill="none" stroke="#222" stroke-width="2"/></svg></div>
<div class="product" style="left:118px;top:2093px"><div class="pimg" style="background:radial-gradient(circle,#d9a26d,#8a4c2a 60%,#fff 71%)" role="img" aria-label="Healthy foods and organs illustration"></div><b>Product Name 01</b><br>$810.00<div class="btn btn-navy">Shop Now</div></div>
<div class="product" style="left:359px;top:2093px"><div class="pimg" style="background:radial-gradient(ellipse 40% 50%,#4b6ca6,#a9bde0 60%,#fff 72%)" role="img" aria-label="Human body cell regeneration illustration"></div><b>Product Name 02</b><br>$810.00<div class="btn btn-navy">Shop Now</div></div>
<div class="product" style="left:600px;top:2093px"><div class="pimg" style="background:radial-gradient(circle,#ffd24a,#e07a10 45%,#3a2410 65%,#fff 72%)" role="img" aria-label="Glowing brain illustration"></div><b>Product Name 03</b><br>$810.00<div class="btn btn-navy">Shop Now</div></div>
<div class="product" style="left:841px;top:2093px"><div class="pimg" style="background:linear-gradient(90deg,#e4c3ad,#c99a80)" role="img" aria-label="Woman with smooth skin portrait"></div><b>Product Name 04</b><br>$810.00<div class="btn btn-navy">Shop Now</div></div>

<!-- blog -->
<svg class="abs" style="left:0;top:2510px" width="1200" height="625" viewBox="0 0 1200 625"><path d="M0,15 C400,-10 800,95 1200,85 L1200,565 C800,555 400,650 0,610 Z" fill="#1aa98a"/></svg>
<h2 class="section-title" style="top:2604px;color:#fff">Our Blog</h2>
<article class="card" style="left:118px"><div class="cimg" style="background:linear-gradient(90deg,#c9d3e0,#e9d7cc)" role="img" aria-label="Regenerative medicine article image"><div class="badge">01<br>Oct</div></div><h3>Regenerative Medicine</h3><div class="meta"><span>◷ Oct 01, 2018</span><span>♡ 20 &nbsp;▢ 03</span></div><p>Lorem Ipsum is simply a is dummy text of the printing and typesetting industry.</p><div class="more">Read More ›</div></article>
<article class="card" style="left:448px"><div class="cimg" style="background:linear-gradient(90deg,#d7dde3,#e6c7b2)" role="img" aria-label="Skin rejuvenation treatment in clinic"><div class="badge">02<br>Oct</div></div><h3>Skin Rejuvenation</h3><div class="meta"><span>◷ Oct 02, 2018</span><span>♡ 20 &nbsp;▢ 03</span></div><p>Lorem Ipsum is simply a is dummy text of the printing and typesetting industry.</p><div class="more">Read More ›</div></article>
<article class="card" style="left:775px"><div class="cimg" style="background:linear-gradient(90deg,#e7e9ea,#3e8f7e)" role="img" aria-label="Doctors consulting in a clinic"><div class="badge">03<br>Nov</div></div><h3>Regenerative Medicine</h3><div class="meta"><span>◷ Sep 01, 2018</span><span>♡ 20 &nbsp;▢ 03</span></div><p>Lorem Ipsum is simply a is dummy text of the printing and typesetting industry.</p><div class="more">Read More ›</div></article>
<div class="btn btn-navy" style="left:520px;top:3082px;width:160px">View More</div>

<!-- testimonials -->
<h2 class="section-title" style="top:3264px;font-size:24px">Testimonials</h2>
<div class="abs" style="left:0;top:3306px;width:1200px;text-align:center;font-size:12px">Lorem Ipsum is simply dummy text of the printing.</div>
<div class="tcard" style="left:118px"><div class="avatar" style="background:linear-gradient(135deg,#e9d3be,#c39a7d)" role="img" aria-label="Client portrait"></div><span class="qmark" style="left:168px;top:20px">“</span><div class="who">Daniel Marsh</div><div class="role">Director</div><div class="quote">Lorem Ipsum is simply dummy text of the typesetting industry. Lorem has the industry's standard</div><div class="read">Read More.. ›</div></div>
<div class="tcard" style="left:619px"><div class="avatar" style="background:linear-gradient(135deg,#ecdcd2,#c9a590)" role="img" aria-label="Client portrait"></div><div class="who">Daniel Marsh</div><div class="role">Director</div><div class="quote">Lorem Ipsum is simply dummy text of the typesetting industry. Lorem has the industry's standard</div><div class="read">Read More.. ›</div><span class="qmark" style="left:420px;top:108px">”</span></div>
<div class="abs dots" style="left:573px;top:3586px"><i></i><i class="on" style="background:var(--green)"></i><i class="on"></i></div>

<!-- newsletter -->
<h2 class="section-title" style="top:3626px;font-size:24px">Join The Newsletter</h2>
<div class="abs" style="left:0;top:3660px;width:1200px;text-align:center;font-size:12px">Sign up for Our Newsletter</div>
<div class="abs" style="left:339px;top:3690px;width:383px;height:30px;background:var(--light);border-radius:15px 0 0 15px;font-size:12px;padding:8px 16px;color:#777">Email here</div>
<div class="btn btn-navy" style="left:722px;top:3690px;width:124px;border-radius:0 15px 15px 0">Submit</div>

<!-- features -->
<div class="feature" style="left:118px"><svg class="abs" style="left:124px;top:36px" width="60" height="50" viewBox="0 0 60 50"><path d="M2 30l20-4 18-22c3-3 8-2 6 3L34 26l20 6v6L32 33 20 44h-6l6-13-16 2z" fill="#222"/></svg><div class="ft">Free Shipping Worldwide</div><div class="fs">Order Over USD 15 7days week</div></div>
<div class="feature" style="left:448px;background:var(--green);color:#fff"><svg class="abs" style="left:130px;top:30px" width="48" height="56" viewBox="0 0 48 56"><circle cx="24" cy="16" r="11" fill="#fff"/><path d="M4 54c0-14 9-22 20-22s20 8 20 22z" fill="#fff"/><path d="M10 18a14 14 0 0128 0" fill="none" stroke="#fff" stroke-width="3"/></svg><div class="ft">24/7 Customer Services</div><div class="fs">Call us 24/7 at 000 123 4567</div></div>
<div class="feature" style="left:775px"><svg class="abs" style="left:128px;top:34px" width="52" height="52" viewBox="0 0 52 52"><path d="M26 3a22 20 0 110 40c-3 0-6 0-8-1L6 48l4-11A20 20 0 0126 3z" fill="#222"/><text x="26" y="31" font-size="22" text-anchor="middle" fill="#fff" font-family="Lora,serif">?</text></svg><div class="ft">Product Guide</div><div class="fs">How to Shop</div></div>

<!-- footer -->
<svg class="abs" style="left:0;top:3995px" width="1200" height="40" viewBox="0 0 1200 40"><path d="M0,10 C400,0 800,30 1200,8 L1200,40 L0,40 Z" fill="#1aa98a"/></svg>
<footer class="abs footer">
  <div class="abs" style="left:118px;top:58px;display:flex;align-items:center;gap:10px"><span style="width:36px;height:36px;border-radius:50%;background:var(--green);display:block"></span><span style="font-size:34px;font-weight:600;color:#fff;letter-spacing:2px">Varden</span></div>
  <p class="abs" style="left:118px;top:172px;width:250px;font-size:12.5px;line-height:19px">Lorem Ipsum is simply dummy text the printing and typesetting industry has been the industry's.</p>
  <div class="abs" style="left:118px;top:252px;display:flex;gap:6px"><i style="width:38px;height:24px;background:#e8e8e8;display:block"></i><i style="width:38px;height:24px;background:#e8e8e8;display:block"></i><i style="width:38px;height:24px;background:#e8e8e8;display:block"></i><i style="width:38px;height:24px;background:#e8e8e8;display:block"></i></div>

  <div class="abs fhead" style="left:413px;top:104px">Quick Links</div>
  <ul class="abs flist" style="left:413px;top:140px"><li>Home</li><li>About us</li><li>Services</li><li>Products</li><li>Blogs</li><li>Testimonials</li><li>Contact us</li></ul>

  <div class="abs fhead" style="left:619px;top:104px">Office</div>
  <div class="abs finfo" style="left:619px;top:140px">
    <div style="display:flex;gap:12px"><svg width="14" height="18" viewBox="0 0 14 18" style="margin-top:4px"><path d="M7 0a7 7 0 017 7c0 5-7 11-7 11S0 12 0 7a7 7 0 017-7z" fill="#fff"/><circle cx="7" cy="7" r="2.5" fill="#1d1d1d"/></svg><span style="line-height:18px">48 Larkmoor Avenue,<br>Pasadena, USA<br>CA 91101</span></div>
    <div style="display:flex;gap:12px;margin-top:4px"><svg width="14" height="14" viewBox="0 0 14 14" style="margin-top:6px"><path d="M3 0l3 3-2 2c1 2 3 4 5 5l2-2 3 3-2 3C6 14 0 8 0 3z" fill="#fff"/></svg>800.555.0142</div>
    <div style="display:flex;gap:12px"><svg width="14" height="10" viewBox="0 0 14 10" style="margin-top:8px"><rect width="14" height="10" fill="#fff"/><path d="M0 0l7 6 7-6" fill="none" stroke="#1d1d1d"/></svg>info@vardenrc.example</div>
    <div style="display:flex;gap:12px"><svg width="14" height="14" viewBox="0 0 14 14" style="margin-top:6px"><circle cx="7" cy="7" r="6" fill="none" stroke="#fff" stroke-width="2"/><path d="M7 3v4h3" stroke="#fff" stroke-width="1.5" fill="none"/></svg>Mon–Sat 9:00am–6:00pm</div>
  </div>

  <div class="abs fhead" style="left:811px;top:104px">Quick Contact</div>
  <div class="field" style="left:811px;top:144px;width:128px">Name</div>
  <div class="field" style="left:948px;top:144px;width:128px">Phone</div>
  <div class="field" style="left:811px;top:180px;width:265px;height:60px">Message</div>
  <div class="btn btn-navy" style="left:958px;top:252px;width:118px;height:26px;border-radius:13px">Send</div>
</footer>
<div class="abs bottom">
  <div class="abs" style="left:118px;top:21px">© Copyright 2018 Varden. All Rights Reserved</div>
  <span class="social" style="left:902px"></span><span class="social" style="left:938px"></span><span class="social" style="left:974px"></span><span class="social" style="left:1010px"></span><span class="social" style="left:1046px"></span>
</div>

</div>
</body>
</html>
```